Maplebrook Self Storage - Business Sign

The sign we are needing designed is our main road sign for our self-storage business. The dimensions of the sign are 57 inches tall x 96 inches wide. We require that our attached logo be on the sign as well as our phone number: 478-216-7745 and website www.MaplebrookStorage.net. Optional information that can be added but not required is our address: 418 Delmont Ridge Pkwy, Centerville, GA 31044.

Industry/Entity Type

Self Storage

Font styles to use
Sans Serif

```html
<!DOCTYPE html>
<html lang="en">
<head>
<meta charset="utf-8">
<title>Maplebrook Self Storage – Road Sign</title>
<link rel="stylesheet" href="https://fonts.googleapis.com/css2?family=Roboto:wght@700&display=swap">
<style>
  :root {
    --backdrop: #e7eaee;
    --panel: #ffffff;
    --brand-blue: #1b80e2;
    --band-end: #1469c9;
    --mark-tone: #c9dff7;
    --ink: #444444;
    --on-blue: #ffffff;
  }
  * { margin: 0; padding: 0; box-sizing: border-box; }
  html, body {
    width: 1200px;
    height: 871px;
    overflow: hidden;
    background: var(--backdrop);
    font-family: "Roboto", Arial, sans-serif;
    font-weight: 700;
  }
  .sign {
    position: absolute;
    left: 50px;
    top: 109px;
    width: 1100px;
    height: 653px;
    background: var(--panel);
    box-shadow: 0 2px 10px rgba(0,0,0,0.12);
  }
  .brand-symbol {
    position: absolute;
    left: 498px;
    top: 36px;
    width: 104px;
    height: 104px;
    background: var(--mark-tone);
  }
  .brand-name {
    position: absolute;
    left: 0;
    top: 150px;
    width: 100%;
    text-align: center;
    color: var(--ink);
    line-height: 1;
    font-weight: 700;
  }
  .brand-name__primary {
    display: block;
    font-size: 136px;
    letter-spacing: -1px;
  }
  .brand-name__secondary {
    display: block;
    margin-top: 14px;
    font-size: 62px;
    letter-spacing: 20px;
    padding-left: 20px;
  }
  .phone-band {
    position: absolute;
    left: 0;
    top: 423px;
    width: 100%;
    height: 112px;
    background: var(--brand-blue);
  }
  .phone-band__end {
    position: absolute;
    top: 16px;
    width: 140px;
    height: 80px;
    background: var(--band-end);
  }
  .phone-band__end--left { left: 0; }
  .phone-band__end--right { right: 0; }
  .phone-band__number {
    position: absolute;
    left: 0;
    top: 0;
    width: 100%;
    line-height: 112px;
    text-align: center;
    color: var(--on-blue);
    font-size: 100px;
    letter-spacing: 1px;
  }
  .website {
    position: absolute;
    left: 0;
    top: 557px;
    width: 100%;
    text-align: center;
    color: var(--ink);
    font-size: 66px;
    line-height: 74px;
  }
</style>
</head>
<body>
  <main class="sign">
    <div class="brand-symbol" role="img" aria-label="Brand symbol area"></div>
    <h1 class="brand-name">
      <span class="brand-name__primary">Maplebrook</span>
      <span class="brand-name__secondary">SELF STORAGE</span>
    </h1>

    <div class="phone-band">
      <div class="phone-band__end phone-band__end--left"></div>
      <div class="phone-band__end phone-band__end--right"></div>
      <p class="phone-band__number">478-216-7745</p>
    </div>

    <p class="website">www.MaplebrookStorage.net</p>
  </main>
</body>
</html>
```